Masonry and Landscaping Construction company business card

Looking for a business card design for a construction company named Ferrano Construction. It is an italian-american family business that specializes in custom stone work, patios, walkways, driveways, steps, outdoor kitchens, concrete, waterproofing, power wash, landscaping and more. Our colors are mostly red and white with some black. We're looking for a bold design. we also like to incorporate a picture of my family's hometown somewhere in it.
Target Market(s)
Luxury home owners
Industry/Entity Type
Construction
Contact Information for Business Card
Details includes should be bullet points mentioning the services provided. Custom Stone Work, Outdoor Kitchens, Fire Pits, Patios, Walkways, Steps, Concrete, Waterproofing, powerwash and landscaping
Requirements
Must have
- Would like a spot on the card for co-owners names, numbers and email to be listed also looking to add the QR code for an instagram page
Nice to have
- would like something bold, based around the colors red and white with black outlines or details

```html
<!DOCTYPE html>
<html lang="en">
<head>
<meta charset="utf-8">
<title>Ferrano Construction – Business Card</title>
<link href="https://fonts.googleapis.com/css2?family=Open+Sans:wght@400;600;700;800&display=swap" rel="stylesheet">
<style>
  :root {
    --red: #e8102f;
    --red-deep: #c70a22;
    --red-soft: #f23a55;
    --white: #ffffff;
    --ink: #222222;
    --green: #2fbf4a;
    --ghost: #efefef;
    --stage: #2e2e2e;
  }
  * { box-sizing: border-box; margin: 0; padding: 0; }
  html, body {
    width: 1200px; height: 875px; overflow: hidden;
    background: var(--stage);
    font-family: "Open Sans", Arial, sans-serif;
  }
  .sheet {
    width: 1200px; height: 875px;
    display: flex; flex-direction: column; align-items: center; justify-content: center;
    gap: 22px;
  }
  .card {
    position: relative;
    width: 720px; height: 411px;
    border-radius: 22px;
    overflow: hidden;
  }

  /* Front */
  .card-front { background: var(--red); color: var(--white); }
  .hometown-photo {
    position: absolute; inset: 0;
    background:
      radial-gradient(ellipse at 30% 80%, rgba(150,0,20,0.45), transparent 60%),
      linear-gradient(160deg, var(--red-soft) 0%, var(--red) 45%, var(--red-deep) 100%);
  }
  .front-brand {
    position: absolute; left: 60px; top: 150px; width: 300px;
    display: flex; align-items: center; gap: 14px;
  }
  .brand-mark { width: 22px; height: 22px; background: var(--white); flex: none; }
  .brand-name { font-weight: 800; font-size: 30px; line-height: 1.1; text-transform: uppercase; }
  .divider {
    position: absolute; left: 390px; top: 60px; width: 1.5px; height: 290px;
    background: var(--white);
  }
  .services { position: absolute; left: 420px; top: 62px; list-style: none; }
  .services li {
    display: flex; align-items: center; gap: 10px;
    font-size: 17px; line-height: 28.5px; font-weight: 400;
  }
  .services svg { width: 15px; height: 15px; flex: none; }

  /* Back */
  .card-back { background: var(--white); color: var(--ink); }
  .truck-watermark {
    position: absolute; z-index: 0; left: 30px; top: 236px; width: 660px; height: 175px;
    border-radius: 30px 30px 0 0;
    background: linear-gradient(180deg, rgba(239,239,239,0), var(--ghost));
  }
  .back-content { position: absolute; inset: 0; z-index: 1; }
  .back-brand {
    position: absolute; right: 50px; top: 44px;
    display: flex; align-items: center; gap: 10px;
    color: var(--red);
  }
  .back-brand .brand-mark { background: var(--red); width: 18px; height: 18px; }
  .back-brand .brand-name { font-size: 22px; }
  .rule-top {
    position: absolute; left: 360px; right: 40px; top: 108px; height: 1.5px; background: var(--red);
  }
  .company-block {
    position: absolute; right: 50px; top: 118px; text-align: right;
    font-size: 15px; line-height: 22px; color: var(--ink);
  }
  .company-block .company { color: var(--red); font-weight: 700; font-size: 16px; }
  .person { position: absolute; left: 48px; top: 180px; width: 300px; }
  .person-name {
    color: var(--red); font-weight: 800; font-size: 34px; line-height: 44px;
    letter-spacing: 0.5px; text-transform: uppercase;
  }
  .person-role { color: var(--green); font-size: 17px; line-height: 22px; }
  .rule-name { width: 300px; height: 1.5px; background: var(--red); margin: 10px 0 10px; }
  .contacts { list-style: none; }
  .contacts li {
    display: flex; align-items: center; gap: 12px;
    font-size: 16px; line-height: 26px;
  }
  .contacts svg { width: 14px; height: 14px; flex: none; fill: var(--red); }
</style>
</head>
<body>
<main class="sheet">

  <section class="card card-front">
    <div class="hometown-photo" role="img" aria-label="Red-tinted photograph of the family's Italian hometown on a hillside"></div>
    <div class="front-brand">
      <span class="brand-mark"></span>
      <span class="brand-name">Ferrano Construction</span>
    </div>
    <div class="divider"></div>
    <ul class="services">
      <li><svg viewBox="0 0 16 16"><circle cx="8" cy="8" r="8" fill="#fff"/><path d="M4.5 8.2l2.3 2.3 4.7-4.8" stroke="#e8102f" stroke-width="2" fill="none"/></svg>Custom Stone Work</li>
      <li><svg viewBox="0 0 16 16"><circle cx="8" cy="8" r="8" fill="#fff"/><path d="M4.5 8.2l2.3 2.3 4.7-4.8" stroke="#e8102f" stroke-width="2" fill="none"/></svg>Outdoor Kitchens</li>
      <li><svg viewBox="0 0 16 16"><circle cx="8" cy="8" r="8" fill="#fff"/><path d="M4.5 8.2l2.3 2.3 4.7-4.8" stroke="#e8102f" stroke-width="2" fill="none"/></svg>Fire Pits</li>
      <li><svg viewBox="0 0 16 16"><circle cx="8" cy="8" r="8" fill="#fff"/><path d="M4.5 8.2l2.3 2.3 4.7-4.8" stroke="#e8102f" stroke-width="2" fill="none"/></svg>Patios</li>
      <li><svg viewBox="0 0 16 16"><circle cx="8" cy="8" r="8" fill="#fff"/><path d="M4.5 8.2l2.3 2.3 4.7-4.8" stroke="#e8102f" stroke-width="2" fill="none"/></svg>Walkways</li>
      <li><svg viewBox="0 0 16 16"><circle cx="8" cy="8" r="8" fill="#fff"/><path d="M4.5 8.2l2.3 2.3 4.7-4.8" stroke="#e8102f" stroke-width="2" fill="none"/></svg>Steps</li>
      <li><svg viewBox="0 0 16 16"><circle cx="8" cy="8" r="8" fill="#fff"/><path d="M4.5 8.2l2.3 2.3 4.7-4.8" stroke="#e8102f" stroke-width="2" fill="none"/></svg>Concrete</li>
      <li><svg viewBox="0 0 16 16"><circle cx="8" cy="8" r="8" fill="#fff"/><path d="M4.5 8.2l2.3 2.3 4.7-4.8" stroke="#e8102f" stroke-width="2" fill="none"/></svg>Waterproofing</li>
      <li><svg viewBox="0 0 16 16"><circle cx="8" cy="8" r="8" fill="#fff"/><path d="M4.5 8.2l2.3 2.3 4.7-4.8" stroke="#e8102f" stroke-width="2" fill="none"/></svg>Power Wash</li>
      <li><svg viewBox="0 0 16 16"><circle cx="8" cy="8" r="8" fill="#fff"/><path d="M4.5 8.2l2.3 2.3 4.7-4.8" stroke="#e8102f" stroke-width="2" fill="none"/></svg>Landscaping &amp; More</li>
    </ul>
  </section>

  <section class="card card-back">
    <div class="truck-watermark" role="img" aria-label="Faint grey illustration of a construction dump truck"></div>
    <div class="back-content">
      <div class="back-brand">
        <span class="brand-mark"></span>
        <span class="brand-name">Ferrano Construction</span>
      </div>
      <div class="rule-top"></div>
      <div class="company-block">
        <div class="company">Ferrano Construction</div>
        <div>423 Street Address Here, City</div>
        <div>State &amp; Country, ZIP Code</div>
        <div>www.yourwebsitehere.com</div>
      </div>
      <div class="person">
        <div class="person-name">Luca Bellini</div>
        <div class="person-role">Co-Owners</div>
        <div class="rule-name"></div>
        <ul class="contacts">
          <li><svg viewBox="0 0 16 16"><path d="M3 1l3 0 1 4-2 1a9 9 0 0 0 5 5l1-2 4 1v3c0 1-1 2-2 2A13 13 0 0 1 1 3c0-1 1-2 2-2z"/></svg>(123) 456-7890</li>
          <li><svg viewBox="0 0 16 16"><path d="M4 0h8a1 1 0 0 1 1 1v14a1 1 0 0 1-1 1H4a1 1 0 0 1-1-1V1a1 1 0 0 1 1-1zm1 2v10h6V2z"/></svg>(123) 456-7890</li>
          <li><svg viewBox="0 0 16 16"><path d="M4 0h8v4H4zM1 5h14v7h-3v4H4v-4H1zm4 5v4h6v-4z"/></svg>(123) 456-7890</li>
          <li><svg viewBox="0 0 16 16"><path d="M0 3h16v10H0zm1.5 1.2L8 9l6.5-4.8V4h-13z"/></svg>info@yourwebsitehere.com</li>
        </ul>
      </div>
    </div>
  </section>

</main>
</body>
</html>
```